The website is called gearloftic.net. It's a DIY projects ( only mechanical engineering related projects ) where mechanical engineers/student can share their ideas/ DIY projects/tutorial/course projects/Graduation projects...etc.
The website is more or less like craftivora.net ( please spend some time in this website ), but strictly to mechanical engineer and it will feature projects like pumps, turbines, compressor, gearboxes, automotive ...etc
There will be four categories:
1- Create, it's where the user can share his project, so it will have a writing feature ( title, body , upload image at different locations of the body ...etc)
2- Tutorials, where is user can share a tutorial so it should have a writing feature also
3- Build, where the user can see others projects
4- Buy, two items: a- T-shirts, b-Books ( DIY books made by us )
Notes:
-In the Share and tutorial categories, the user should select subcategory ( Will give them to you later ).
-When clicking to "make" category the user can see all the posted projects, then he can select a sub category ( see partspindle.net )
- each user will have a personal page
- Buy category will be added later if the website succeeded
- landing page feature the latest projects,tutorial
This is the full detail about the website, if there is something specific please let me know.
*No logo is been made yet.
thanks.
Industry/Entity Type
Mechanical Engineering
Look and feel

```html
<!DOCTYPE html>
<html lang="en">
<head>
<meta charset="utf-8">
<title>gearloftic.net – DIY mechanical projects</title>
<link href="https://fonts.googleapis.com/css2?family=Open+Sans:wght@400;600;700&family=PT+Sans+Narrow:wght@400;700&display=swap" rel="stylesheet">
<style>
:root{
  --teal:#1a7fa3;
  --teal-dark:#12627f;
  --teal-deep:#0f5a76;
  --teal-light:#2596bf;
  --ink:#0b0b0b;
  --nav:#161616;
  --head:#1c6f93;
  --text:#555;
  --white:#fff;
  --rule:#dfe4e7;
}
*{margin:0;padding:0;box-sizing:border-box}
html,body{width:938px;height:1200px;overflow:hidden;background:#fff}
body{position:relative;font-family:"Open Sans",Arial,sans-serif;color:var(--text)}
.abs{position:absolute}
.top-band{left:0;top:0;width:938px;height:298px;background:linear-gradient(90deg,var(--teal-dark),var(--teal-light) 55%,var(--teal-dark))}
.brand{left:104px;top:16px;font-family:"PT Sans Narrow",sans-serif;font-weight:700;font-size:36px;letter-spacing:3px;color:var(--white)}
.account{left:754px;top:11px;font-size:10px;color:var(--white)}
.account span{margin:0 5px}
.call{left:413px;top:40px;font-family:"PT Sans Narrow",sans-serif;font-weight:700;font-size:23px;color:var(--white)}
.search{left:649px;top:40px;width:195px;height:26px;background:#fff;border:1px solid #ccc;display:flex;align-items:center;padding:0 9px;font-size:9px;font-style:italic;color:#999;justify-content:space-between}
.nav{left:93px;top:81px;width:751px;height:38px;background:var(--nav);display:flex;align-items:center;list-style:none;border-top:2px solid #3a9ec2}
.nav li{flex:1 1 auto;text-align:center;font-family:"PT Sans Narrow",sans-serif;font-size:13.5px;color:#fff;line-height:36px}
.nav li.active{flex:0 0 80px;background:linear-gradient(180deg,#1f8db5,#156e90)}
.hero{left:78px;top:129px;width:781px;height:293px;background:radial-gradient(ellipse at 70% 50%,#5a4a38,#2a2219 60%,#151210)}
.hero-person{left:150px;top:134px;width:200px;height:270px}
.hero-copy{left:402px;top:256px;width:440px;font-family:"PT Sans Narrow",sans-serif;font-size:21px;line-height:27px;color:#fff}
.arrow{width:36px;height:36px;border-radius:50%;background:rgba(110,110,110,.8)}
.feature{width:180px;height:131px;top:404px;background:var(--teal);border:1px solid #0c4d66;text-align:center;color:#e4f1f6}
.feature h2{font-family:"PT Sans Narrow",sans-serif;font-weight:700;font-size:24px;color:#fff;margin-top:10px}
.feature p{font-size:10px;line-height:14px;height:34px;margin-top:4px;padding:0 14px}
.feature .btn{display:block;margin:8px auto 0;width:162px;height:31px;border-radius:16px;background:var(--ink);color:#fff;font-family:"PT Sans Narrow",sans-serif;font-size:15px;line-height:31px}
.section-title{font-family:"PT Sans Narrow",sans-serif;font-weight:700;font-size:19px;color:var(--head)}
.tile{width:170px;height:153px;background:#ccc;overflow:hidden}
.tile .shot{height:100%}
.tile .cap{position:absolute;left:0;bottom:0;width:100%;height:46px;background:rgba(255,255,255,.85);font-size:9.5px;line-height:12px;color:#222;padding:9px 3px 0 9px;text-align:justify}
.divider{left:650px;top:552px;width:1px;height:354px;background:var(--rule)}
.cats{left:673px;top:578px;width:205px;border-top:1px solid var(--rule);list-style:none;padding-top:8px}
.cats li{font-size:12px;color:#666;height:26.6px}
.cats li::before{content:"››";color:#444;margin-right:9px;font-size:11px}
.pager{left:223px;top:918px;width:401px;height:28px;border-radius:5px;background:linear-gradient(#e8e8e8,#bdbdbd);border:2px solid #d5d5d5;display:flex;align-items:center;justify-content:space-around;font-size:8px;color:#444;padding:0 10px}
.pager .cur{width:15px;height:15px;border-radius:50%;background:#222;color:#fff;text-align:center;line-height:15px}
.footer{left:0;top:963px;width:938px;height:207px;background:linear-gradient(90deg,var(--teal-deep),var(--teal-light) 50%,var(--teal-deep))}
.bottom{left:0;top:1170px;width:938px;height:30px;background:#1b5a73;text-align:center;font-size:10px;color:#fff;line-height:30px}
.f-title{font-family:"PT Sans Narrow",sans-serif;font-size:19px;color:#fff;white-space:nowrap}
.links{list-style:none;font-size:10px;color:#fff}
.links li{height:21.8px}
.news-input{left:411px;top:1020px;width:216px;height:26px;border-radius:13px;background:#fff;font-size:9.5px;color:#999;display:flex;align-items:center;padding-left:34px}
.sub-note{left:470px;top:1057px;width:149px;text-align:right;font-size:9.5px;color:#fff}
.sub-btn{left:550px;top:1082px;width:66px;height:25px;border-radius:13px;background:#1a1a1a;border:1px solid #555;color:#fff;font-weight:700;font-size:12px;text-align:center;line-height:23px}
.bird{left:812px;top:990px;width:28px;height:34px;border-radius:50%;background:linear-gradient(#5bb4e8,#1e6fb0)}
.tweet{left:689px;top:1024px;width:180px;height:90px;border-radius:8px;background:rgba(255,255,255,.12);font-size:9.5px;line-height:16px;color:#fff;padding:12px 15px}
.social{width:24px;height:24px;border-radius:50%;background:rgba(255,255,255,.55)}
</style>
</head>
<body>
<div class="abs top-band"></div>
<div class="abs brand">GEARLOFTIC</div>
<div class="abs account">Login<span>|</span>Register</div>
<div class="abs call">CALL US: 555.014.2290</div>
<div class="abs search">Search here..
  <svg width="13" height="13" viewBox="0 0 13 13"><circle cx="5.5" cy="5.5" r="4" fill="none" stroke="#999" stroke-width="2"/><line x1="8.5" y1="8.5" x2="12" y2="12" stroke="#999" stroke-width="2.4"/></svg>
</div>
<ul class="abs nav">
  <li class="active">HOME</li><li>SERVICES</li><li>PROJECTS</li><li>EXPERTS</li><li>TUTORIALS</li><li>BLOG</li><li>SUCCESS PROJECTS</li><li>HELP</li>
</ul>

<div class="abs hero" role="img" aria-label="Workshop machinery with pipes and valves"></div>
<div class="abs hero-person" role="img" aria-label="Smiling student holding a black folder" style="background:linear-gradient(180deg,#5a3c2a,#c9b7a6 50%,#2a2a2a)"></div>
<div class="abs hero-copy">We are a DIY - Do it yourself mechanical projects collection online for engineering students.</div>
<div class="abs arrow" style="left:741px;top:332px"><svg width="36" height="36"><polygon points="21,12 21,24 13,18" fill="#fff"/></svg></div>
<div class="abs arrow" style="left:786px;top:332px"><svg width="36" height="36"><polygon points="15,12 15,24 23,18" fill="#fff"/></svg></div>

<div class="abs feature" style="left:93px"><h2>CREATE</h2><p>You can share your projects or create and upload images etc</p><span class="btn">CREATE OR SHARE PROJECT</span></div>
<div class="abs feature" style="left:282px"><h2>TUTORIALS</h2><p>You can share your documents and tutorials etc.</p><span class="btn">UPLOAD PROJECT</span></div>
<div class="abs feature" style="left:473px"><h2>BUILD</h2><p>You can see other projects</p><span class="btn">VIEW POJECTS</span></div>
<div class="abs feature" style="left:663px"><h2>BUY</h2><p>Buy Gearloftic T-Shirt or DIY book which we had compiled</p><span class="btn">BUY NOW</span></div>

<h3 class="abs section-title" style="left:97px;top:545px">RECENT PROJECTS</h3>
<div class="abs tile" style="left:96px;top:577px"><div class="shot" role="img" aria-label="Soldering a small circuit board under a magnifier" style="background:linear-gradient(135deg,#6b4c3a,#c9a07e 60%,#e9d8c8)"></div><p class="cap">Sed ut perspiciatis unde omnis iste natus error sit voluptatem</p></div>
<div class="abs tile" style="left:278px;top:577px"><div class="shot" role="img" aria-label="Engineer operating a milling machine" style="background:linear-gradient(135deg,#8f949a,#c8ccd0 50%,#2d5f9a)"></div><p class="cap">Sed ut perspiciatis unde omnis iste natus error sit voluptatem</p></div>
<div class="abs tile" style="left:458px;top:577px"><div class="shot" role="img" aria-label="Gear and lattice crane model" style="background:linear-gradient(135deg,#f2f2f2,#d8d8d8 50%,#2e2e2e)"></div><p class="cap">Sed ut perspiciatis unde omnis iste natus error sit voluptatem</p></div>
<div class="abs tile" style="left:96px;top:746px"><div class="shot" role="img" aria-label="Small walking robot with wires" style="background:linear-gradient(135deg,#d6d6d6,#6a4a4a 50%,#bdbdbd)"></div><p class="cap">Sed ut perspiciatis unde omnis iste natus error sit voluptatem</p></div>
<div class="abs tile" style="left:278px;top:746px"><div class="shot" role="img" aria-label="Centrifugal pump housing" style="background:linear-gradient(135deg,#fafafa,#b9bec4 50%,#7a7f86)"></div><p class="cap">Sed ut perspiciatis unde omnis iste natus error sit voluptatem</p></div>
<div class="abs tile" style="left:458px;top:746px"><div class="shot" role="img" aria-label="Engine pulleys and belts" style="background:linear-gradient(135deg,#5a5d62,#a8acb1 50%,#3c3f44)"></div><p class="cap">Sed ut perspiciatis unde omnis iste natus error sit voluptatem</p></div>

<div class="abs divider"></div>
<h3 class="abs section-title" style="left:673px;top:550px">PROJECTS CATEGORIES</h3>
<ul class="abs cats">
  <li>Etiam eu lectus</li><li>Cras cursus ante</li><li>Pellentesque eget tempor</li><li>Vivamus lacinia</li><li>Nulla tempor dapibus</li><li>Aliquam erat</li><li>Etiam eu lectus</li><li>Cras cursus ante</li><li>Pellentesque eget tempor</li><li>Vivamus lacinia</li><li>Nulla tempor dapibus</li>
</ul>

<div class="abs pager"><span>‹‹ Previous</span><span>1</span><span>2</span><span>3</span><span>4</span><span>5</span><span class="cur">6</span><span>7</span><span>8</span><span>9</span><span>........</span><span>103</span><span>104</span><span>105</span><span>106</span><span>Last ››</span></div>

<div class="abs footer"></div>
<h3 class="abs f-title" style="left:86px;top:981px">QUICK LINK</h3>
<ul class="abs links" style="left:86px;top:1012px"><li>Create</li><li>Tutorials</li><li>Build</li><li>Buy</li><li>Blog</li><li>Projects</li><li>Contact</li></ul>
<ul class="abs links" style="left:174px;top:1012px"><li>Support</li><li>Help</li><li>Career</li><li>Online Course</li><li>Recent projects</li><li>Our Team</li></ul>
<ul class="abs links" style="left:270px;top:1012px"><li>Privacy policy</li><li>Terms And Conditions</li><li>Disclaimer</li><li>Legal Notice</li></ul>

<h3 class="abs f-title" style="left:412px;top:986px">NEWSLETTER SUBSCRIBE</h3>
<div class="abs news-input">Subscribe your news letter</div>
<svg class="abs" style="left:421px;top:1027px" width="18" height="12" viewBox="0 0 18 12"><rect x="0.5" y="0.5" width="17" height="11" fill="none" stroke="#888"/><polyline points="0.5,0.5 9,7 17.5,0.5" fill="none" stroke="#888"/></svg>
<div class="abs sub-note">Subscribe your news letter</div>
<div class="abs sub-btn">Subscribe</div>

<h3 class="abs f-title" style="left:690px;top:988px">CHIRP UPDATES</h3>
<div class="abs bird" role="img" aria-label="Small blue bird mascot"></div>
<div class="abs tweet">@ridgeworks there is a new designer in town people!<br><br>Check it out: http://lnk.gfx</div>
<div class="abs social" style="left:712px;top:1134px"></div>
<div class="abs social" style="left:744px;top:1134px"></div>
<div class="abs social" style="left:777px;top:1134px"></div>
<div class="abs social" style="left:810px;top:1134px"></div>
<div class="abs social" style="left:842px;top:1134px"><svg width="24" height="24"><rect x="6" y="10.5" width="12" height="3" fill="#1a7fa3"/><rect x="10.5" y="6" width="3" height="12" fill="#1a7fa3"/></svg></div>

<div class="abs bottom">© 2013.www.gearloftic.net</div>
</body>
</html>
```